Business Card Design

I am a Special Event Consultant,I arrange and organise Special Events - Product Launches,Sponsorship and Product Displays.

I would like the TRV to be a feature of the design with 'Special Event Services" underneath - keep it very simple but creative using this information. So it is just the letters "TRV" with Event Services underneath.

(Simple Colours - Silver, Black, Grey - no bright colours - We work for Valdoren Kraft,QJX, Tavrelli So it is class and classic.)

Only my Name and mobile on the front.

Industry/Entity Type

Business

Contact Information for Business Card

FRONT
Jo Pettigrew
Tel: 0427 318906

BACK
Email: jo@trvoccasionhire.com.au

1208 Wexley Court,72 Ormond Lane
KELMSTON.Vic.3145.

```html
<!DOCTYPE html>
<html lang="en">
<head>
<meta charset="utf-8">
<title>TRV Event Services – Business Card Back</title>
<link rel="stylesheet" href="https://fonts.googleapis.com/css2?family=Open+Sans:wght@400;600;700&display=swap">
<style>
  :root {
    --page: #ffffff;
    --card-edge: #3a3a3a;
    --card-deep: #0c0c0c;
    --card-mid: #1e1e1e;
    --silver: #b4b4b4;
    --grey-text: #8c8c8c;
  }
  * { margin: 0; padding: 0; box-sizing: border-box; }
  html, body {
    width: 1200px;
    height: 719px;
    overflow: hidden;
    background: var(--page);
  }
  .card {
    position: absolute;
    left: 0;
    top: 0;
    width: 1194px;
    height: 715px;
    border-radius: 30px;
    border-top: 4px solid var(--card-edge);
    border-bottom: 4px solid var(--card-edge);
    background: radial-gradient(ellipse at 50% 30%, var(--card-mid) 0%, var(--card-deep) 75%);
    overflow: hidden;
    font-family: "Open Sans", Arial, sans-serif;
  }
  .card-texture {
    position: absolute;
    inset: 0;
  }
  .brand-name,
  .brand-tagline {
    position: absolute;
    left: 0;
    width: 100%;
    text-align: center;
    line-height: 1;
    color: var(--silver);
    white-space: nowrap;
  }
  .brand-name {
    top: 189px;
    font-size: 164px;
    font-weight: 700;
    letter-spacing: 22px;
    text-indent: 22px;
  }
  .brand-tagline {
    top: 388px;
    font-size: 55px;
    font-weight: 600;
    letter-spacing: 1px;
  }
  .contact {
    position: absolute;
    font-size: 22px;
    line-height: 1;
    color: var(--grey-text);
    white-space: nowrap;
  }
  .contact-email {
    left: 110px;
    top: 620px;
  }
  .contact-address {
    right: 104px;
    top: 584px;
    text-align: right;
    font-style: normal;
  }
  .contact-address span {
    display: block;
    margin-bottom: 14px;
  }
</style>
</head>
<body>
  <section class="card">
    <div class="card-texture" role="img" aria-label="Fine dotted carbon texture across the black card"></div>
    <h1 class="brand-name">TRV</h1>
    <p class="brand-tagline">EVENT SERVICES</p>
    <p class="contact contact-email">jo@trvoccasionhire.com.au</p>
    <address class="contact contact-address">
      <span>1208 Wexley Court</span>
      <span>72 Ormond Lane. KELMSTON. Vic. 3145.</span>
    </address>
  </section>
</body>
</html>
```